Business cards / Letterheads / Compliment slips

We are looking to get business cards, letterheads and compliment slips designed.

These will all have to follow the design of our new website and logo. Links to the website, logo and fonts can be found below...

The designs need to be simple with focus on the typography. Only the following colours should be used on the designs...

#7f9d3c
#191818
#fff

Website:
http://brookfieldweb.examplestudio.co.uk/

Logo:
https://www.filecrate.example/sh/8kd2m4qwzpla7ve/hTr5NpQ2Xw/logos

Fonts:
https://www.filecrate.example/sh/8kd2m4qwzpla7ve/Q9vTzR3mKe/Fonts/BayerModern_TTF

and

https://www.filecrate.example/sh/8kd2m4qwzpla7ve/W7nHcY5pD3/Fonts/MuseoSansFamily

Reason: We would like some more design submissions

Reason: We are still deciding on designs we like and would like to see some more submissions...

Industry/Entity Type

Business

Requirements
Must have
• The designs need to be simple with focus on the typography. Only the following colours should be used on the designs...

#7f9d3c
#191818
#fff
Should not have
• - Any fonts that are not provided.
- Any colours that are not provided.

```html
<!DOCTYPE html>
<html lang="en">
<head>
<meta charset="utf-8">
<title>brookfieldweb stationery</title>
<link rel="stylesheet" href="https://fonts.googleapis.com/css2?family=Nunito+Sans:wght@400;600;700&family=Cinzel:wght@600&display=swap">
<style>
  :root {
    --green: #7f9d3c;
    --ink: #191818;
    --paper: #ffffff;
    --stage: #8a5a36;
    --body-text: #3a3939;
    --card-dark: #3d3d3d;
  }
  * { box-sizing: border-box; margin: 0; padding: 0; }
  html, body { width: 1200px; height: 750px; overflow: hidden; }
  body {
    background: var(--stage);
    font-family: "Nunito Sans", Arial, sans-serif;
    color: var(--ink);
    position: relative;
  }
  .sheet { position: absolute; background: var(--paper); box-shadow: 0 4px 14px rgba(0,0,0,.35); }

  .masthead { position: absolute; display: flex; align-items: center; }
  .brand { display: flex; align-items: center; gap: 6px; white-space: nowrap; }
  .brand-dot { border-radius: 50%; border: 5px solid var(--green); flex: none; }
  .brand-name { color: var(--green); font-weight: 700; letter-spacing: -0.5px; line-height: 1; }

  .contact {
    border-left: 2px solid var(--ink);
    padding-left: 7px;
    line-height: 1.25;
    color: var(--ink);
    white-space: nowrap;
  }

  /* Letterhead */
  .letterhead { left: 67px; top: 42px; width: 517px; height: 666px; }
  .letterhead .masthead { left: 34px; top: 34px; gap: 20px; }
  .letterhead .brand-dot { width: 40px; height: 40px; border-width: 6px; }
  .letterhead .brand-name { font-size: 23px; }
  .letterhead .contact { font-size: 9.5px; }
  .letter-body {
    position: absolute; left: 49px; top: 125px; width: 430px;
    font-size: 8.4px; line-height: 1.52; color: var(--body-text);
  }
  .letter-body p { margin-bottom: 9px; }
  .letter-body p.gap { margin-top: 20px; }
  .sign-off { position: absolute; left: 49px; top: 566px; font-size: 8.4px; color: var(--body-text); }
  .signature {
    position: absolute; left: 49px; top: 580px; width: 100px; height: 46px;
    background: linear-gradient(90deg, #e8e8e8, #f4f4f4);
  }

  /* Business cards */
  .card { width: 210px; height: 118px; border-radius: 4px; }
  .card-front { left: 654px; top: 256px; background: var(--card-dark); }
  .card-front .brand { position: absolute; left: 30px; top: 42px; }
  .card-front .brand-dot { width: 30px; height: 30px; border-width: 4px; }
  .card-front .brand-name { font-size: 17px; }
  .card-front .web { position: absolute; left: 0; right: 0; bottom: 8px; text-align: center; color: var(--paper); font-size: 7px; }

  .card-back { left: 884px; top: 256px; }
  .card-back .brand { position: absolute; left: 30px; top: 12px; }
  .card-back .brand-dot { width: 28px; height: 28px; border-width: 4px; }
  .card-back .brand-name { font-size: 17px; }
  .person { position: absolute; right: 108px; top: 79px; text-align: right; }
  .person-name { color: var(--green); font-weight: 700; font-size: 8.5px; }
  .person-role { font-size: 5.5px; color: var(--ink); }
  .card-back .contact { position: absolute; left: 108px; top: 79px; font-size: 5.8px; border-left-width: 1px; padding-left: 5px; }

  /* Compliment slip */
  .comp-slip { left: 616px; top: 406px; width: 516px; height: 235px; }
  .comp-slip .masthead { left: 26px; top: 24px; gap: 18px; }
  .comp-slip .brand-dot { width: 36px; height: 36px; }
  .comp-slip .brand-name { font-size: 20px; }
  .comp-slip .contact { font-size: 9px; }
  .comp-title {
    position: absolute; right: 32px; bottom: 36px;
    font-family: "Cinzel", Georgia, serif; font-weight: 600;
    color: var(--green); font-size: 21px; letter-spacing: 1px;
  }
</style>
</head>
<body>

<section class="sheet letterhead">
  <div class="masthead">
    <div class="brand">
      <span class="brand-dot"></span>
      <span class="brand-name">brookfieldweb</span>
    </div>
    <div class="contact">
      P. +00 123 456 789<br>
      F. +00 123 456 789<br>
      office@brookfieldweb.co.uk
    </div>
  </div>
  <div class="letter-body">
    <p>Lorem Ipsum is simply dummy text of the printing and typesetting industry. Lorem Ipsum has been the industry's standard dummy text ever since the 1500s, when an unknown printer took a galley of type and scrambled it to make a type specimen book. It has survived not only five centuries, but also the leap into electronic typesetting, remaining essentially unchanged. It was popularised in the 1960s with the release of Letterform sheets containing Lorem Ipsum passages, and more recently with desktop publishing software like Pagewright Studio including versions of Lorem Ipsum.</p>
    <p>It is a long established fact that a reader will be distracted by the readable content of a page when looking at its layout. The point of using Lorem Ipsum is that it has a more-or-less normal distribution of letters, as opposed to using 'Content here, content here', making it look like readable English. Many desktop publishing packages and web page editors now use Lorem Ipsum as their default model text, and a search for 'lorem ipsum' will uncover many web sites still in their infancy. Various versions have evolved over the years, sometimes by accident, sometimes on purpose (injected humour and the like).</p>
    <p class="gap">Contrary to popular belief, Lorem Ipsum is not simply random text. It has roots in a piece of classical Latin literature from 45 BC, making it over 2000 years old. Robert Whitlock, a Latin professor at Harwood Vale College in Virginia, looked up one of the more obscure Latin words, consectetur, from a Lorem Ipsum passage, and going through the cites of the word in classical literature, discovered the undoubtable source. Lorem Ipsum comes from sections 1.10.32 and 1.10.33 of "de Finibus Bonorum et Malorum" (The Extremes of Good and Evil) by Marcus, written in 45 BC. This book is a treatise on the theory of ethics, very popular during the Renaissance. The first line of Lorem Ipsum, "Lorem ipsum dolor sit amet..", comes from a line in section 1.10.32.</p>
    <p>The standard chunk of Lorem Ipsum used since the 1500s is reproduced below for those interested. Sections 1.10.32 and 1.10.33 from "de Finibus Bonorum et Malorum" by Marcus are also reproduced in their exact original form, accompanied by English versions from the 1914 translation by H. Rowley.</p>
    <p>There are many variations of passages of Lorem Ipsum available, but the majority have suffered alteration in some form, by injected humour, or randomised words which don't look even slightly believable. If you are going to use a passage of Lorem Ipsum, you need to be sure there isn't anything embarrassing hidden in the middle of text. All the Lorem Ipsum generators on the Internet tend to repeat predefined chunks as necessary, making this the first true generator on the Internet. It uses a dictionary of over 200 Latin words, combined with a handful of model sentence structures, to generate Lorem Ipsum which looks reasonable. The generated Lorem Ipsum is therefore always free from repetition, injected humour, or non-characteristic words etc.</p>
  </div>
  <div class="sign-off">Regards,</div>
  <div class="signature" role="img" aria-label="Handwritten signature"></div>
</section>

<section class="sheet card card-front">
  <div class="brand">
    <span class="brand-dot"></span>
    <span class="brand-name">brookfieldweb</span>
  </div>
  <div class="web">www.brookfieldweb.co.uk</div>
</section>

<section class="sheet card card-back">
  <div class="brand">
    <span class="brand-dot"></span>
    <span class="brand-name">brookfieldweb</span>
  </div>
  <div class="person">
    <div class="person-name">Name Surname</div>
    <div class="person-role">manager</div>
  </div>
  <div class="contact">
    P. +00 123 456 789<br>
    F. +00 123 456 789<br>
    office@brookfieldweb.co.uk
  </div>
</section>

<section class="sheet comp-slip">
  <div class="masthead">
    <div class="brand">
      <span class="brand-dot"></span>
      <span class="brand-name">brookfieldweb</span>
    </div>
    <div class="contact">
      P. +00 123 456 789<br>
      F. +00 123 456 789<br>
      office@brookfieldweb.co.uk
    </div>
  </div>
  <div class="comp-title">With Compliments</div>
</section>

</body>
</html>
```